Vantor Health Group Presentation Folder, for Cancer Awareness, VERY COLORFUL AND MODERN

Presentation Folder I know pretty much what i want so it should be very eazy , I have included files from folders I use now rebrand them to my new company they will be fine, no sense re creating the wheel
Full Bleed Size
20.87" x 16.68"
53 x 42.4 cm
6260 x 5004 pixels
Document Trim Size
20.75" x 16.56"
52.7 x 42.1 cm
6225 x 4969 pixels
Updates

Low design quality

Industry/Entity Type

Medical

Font styles to use
Serif

Colors

Designer to choose colors to be used in the design.

Requirements
Must have
• really I am not looking for some one to redesign, we like our folder front page and would like to see new word information added., there are two folder front pages to choose from
• So Keep the original front page and redesign the back page and the pockets
• Can Make your Design off of one of the ones I already uploaded
Nice to have
• Keep the same color schemes, Keep the original front page and redesign the back page and the pockets
Should not have
• DO not recreate the front covers, use what I gave you and just rebrand

```html
<!DOCTYPE html>
<html lang="en">
<head>
<meta charset="utf-8">
<title>Vantor Health Group – Hereditary Cancer Screening Folder</title>
<link href="https://fonts.googleapis.com/css2?family=Raleway:wght@300;400;500&display=swap" rel="stylesheet">
<style>
  :root{
    --paper:#ffffff;
    --cut:#e0434f;
    --fold:#4cc28a;
    --pink:#f497a8;
    --band:#6d6e71;
    --band-light:#a7a9ac;
    --strip:#d1d3d4;
    --ink:#58595b;
    --brand:#1f3a7a;
  }
  *{margin:0;padding:0;box-sizing:border-box}
  html,body{width:1200px;height:964px;overflow:hidden;background:var(--paper)}
  .folder{position:relative;width:1200px;height:964px;font-family:"Raleway",sans-serif;color:var(--ink)}
  .dieline{position:absolute;inset:0}
  .abs{position:absolute}
  .photo{position:absolute}
  .photo--beach{left:124px;top:304px;width:474px;height:254px;
    background:
      radial-gradient(ellipse 60% 55% at 50% 62%, rgba(120,112,108,.55) 0%, rgba(120,112,108,0) 70%),
      linear-gradient(180deg,#ffffff 0%,#f3f1ef 22%,#e4e0dc 42%,#bdb6b1 56%,#d3cdc8 62%,#9e9691 76%,#7b736f 90%,#6a625e 100%)}
  .photo--table{left:600px;top:260px;width:475px;height:310px;
    background:
      radial-gradient(ellipse 55% 45% at 55% 40%, rgba(150,140,134,.55) 0%, rgba(150,140,134,0) 70%),
      radial-gradient(ellipse 45% 40% at 65% 85%, rgba(190,184,178,.7) 0%, rgba(190,184,178,0) 70%),
      linear-gradient(180deg,#f7f6f5 0%,#e6e2df 20%,#c9c2bd 45%,#a8a09b 65%,#bdb6b0 80%,#8f8782 100%)}
  .caption{position:absolute;left:124px;top:558px;width:474px;height:48px;background:var(--band);
    color:#fff;font-size:12.5px;font-weight:400;letter-spacing:1px;line-height:14px;text-align:center;padding-top:6px}
  .title-band{left:600px;top:123px;width:475px;height:39px;background:var(--pink);color:#fff;
    font-size:20px;font-weight:400;letter-spacing:3px;text-align:center;line-height:39px}
  .sub-band{left:650px;top:162px;width:375px;height:31px;background:var(--band-light);color:#fff;
    font-size:10.5px;font-weight:400;letter-spacing:1.6px;text-align:center;line-height:31px}
  .intro{left:632px;top:199px;width:410px;font-size:10.5px;font-weight:400;line-height:13.5px;text-align:center}
  .tagline{left:600px;top:573px;width:475px;height:33px;background:var(--band);color:#fff;
    font-size:14px;font-weight:400;letter-spacing:1px;text-align:center;line-height:33px}
  .brand{display:flex;align-items:center;gap:6px;font-weight:500;color:var(--brand)}
  .brand--front{left:638px;top:618px;font-size:12px;line-height:12.5px;letter-spacing:.4px}
  .brand__dot{width:38px;height:38px;border-radius:50%;background:var(--brand)}
  .flip{transform:rotate(180deg)}
  .brand--pocket{left:250px;top:682px;width:222px;color:#fff;flex-direction:column;align-items:flex-start;gap:3px}
  .brand--pocket .row{display:flex;align-items:center;gap:6px;font-size:16px;font-weight:400}
  .brand--pocket .dot{width:29px;height:29px;border-radius:50%;background:#fff}
  .brand--pocket .division{align-self:flex-end;font-size:9.5px;font-weight:400;letter-spacing:.2px}
  .pocket-copy{left:686px;top:742px;width:298px;color:#fff;font-size:10.8px;line-height:13.6px;text-align:justify}
</style>
</head>
<body>
<div class="folder">
  <svg class="dieline" width="1200" height="964" viewBox="0 0 1200 964">
    <path d="M128,670 L128,892 L540,892 Q562,892 566,872 L597,670 Z" fill="var(--band)"/>
    <rect x="128" y="670" width="32" height="222" fill="var(--strip)"/>
    <path d="M603,670 L634,872 Q638,892 660,892 L1074,892 L1074,670 Z" fill="var(--band)"/>
    <rect x="1042" y="670" width="32" height="222" fill="var(--strip)"/>
    <path d="M128,670 L128,892 L540,892 Q562,892 566,872 L597,670 M603,670 L634,872 Q638,892 660,892 L1074,892 L1074,670" fill="none" stroke="var(--cut)" stroke-width="0.8"/>
    <g stroke="#fff" stroke-width="0.8">
      <line x1="272" y1="760" x2="302" y2="730"/>
      <line x1="420" y1="730" x2="450" y2="760"/>
      <line x1="272" y1="804" x2="302" y2="834"/>
      <line x1="420" y1="834" x2="450" y2="804"/>
    </g>
    <path d="M124,74 L1076,74 M124,74 L88,78 L88,430 A18,18 0 0 1 88,466 L88,665 L124,670 M1076,74 L1112,78 L1112,430 A18,18 0 0 0 1112,466 L1112,665 L1076,670" fill="none" stroke="var(--cut)" stroke-width="0.8"/>
    <g stroke="var(--fold)" stroke-width="0.8" stroke-dasharray="3 3">
      <line x1="124" y1="74" x2="124" y2="669"/>
      <line x1="600" y1="74" x2="600" y2="669"/>
      <line x1="1076" y1="74" x2="1076" y2="669"/>
      <line x1="124" y1="669" x2="1076" y2="669"/>
    </g>
  </svg>

  <div class="photo photo--beach" role="img" aria-label="Black-and-white photo of a multigenerational family holding hands on a beach, seen from behind"></div>
  <p class="caption">Don't be Afraid of the Answer: Knowledge is Power and<br>Power Eradicates Fear. When You are Fearless, You Will Make<br>all the Right Choices!</p>

  <h1 class="abs title-band">HEREDITARY CANCER SCREENING</h1>
  <h2 class="abs sub-band">DOCTORS ARE THE GATEKEEPERS TO GENETIC TESTING</h2>
  <p class="abs intro">We have an obligation to help patients understand genetic risk and how testing<br>can guide heath care decisions.</p>
  <div class="photo photo--table" role="img" aria-label="Black-and-white photo of a family sharing a meal at an outdoor table"></div>
  <p class="abs tagline">The test you order FOR your patients</p>
  <div class="abs brand brand--front"><span class="brand__dot"></span><span>VANTOR<br>HEALTH<br>GROUP</span></div>

  <div class="abs brand brand--pocket flip">
    <div class="row"><span class="dot"></span><span>Vantor Health Group</span></div>
    <span class="division">a division of Meridian Clinical Sales LLC</span>
  </div>
  <p class="abs pocket-copy flip">At our state of the art, CLIA certified and COLA accredited facility we perform Next Generation Sequencing (NGS) based screening for mutations known to affect an individual's Risk of developing Hereditary Cancer. Results from the test enable the Physician to make Better informed treatment decisions.</p>
</div>
</body>
</html>
```